Tidewell Provisions

Distributor of seasonings and spices to the restaurant industry.

Restaurant

Tidewell Provis
Dean Holcroft
TK Wandsley Distributor
317-640-8917
dean@tidewellprovisionsco.com

No minimum order
Gluten & MSG free soup bases

```html
<!DOCTYPE html>
<html lang="en">
<head>
<meta charset="utf-8">
<title>Tidewell Provisions — Business Card</title>
<link href="https://fonts.googleapis.com/css2?family=Dancing+Script:wght@700&family=Open+Sans:wght@400;600&display=swap" rel="stylesheet">
<style>
  :root {
    --page: #ece9e4;
    --card: #ffffff;
    --ink: #2b2b2b;
    --ink-soft: #4a4a4a;
    --band: #262626;
    --accent-orange: #ee6a45;
    --accent-yellow: #f2e21c;
  }
  * { margin: 0; padding: 0; box-sizing: border-box; }
  html, body { width: 1200px; height: 1023px; overflow: hidden; background: var(--page); }
  .card {
    position: absolute;
    left: 180px; top: 271px;
    width: 840px; height: 480px;
    background: var(--card);
    box-shadow: 0 10px 30px rgba(0,0,0,0.18);
    overflow: hidden;
    font-family: "Open Sans", sans-serif;
    color: var(--ink);
  }
  .card__band { position: absolute; inset: 0; width: 840px; height: 480px; }
  .brand {
    position: absolute;
    left: 50px; top: 170px;
    display: flex; align-items: center; gap: 14px;
  }
  .brand__dot {
    width: 46px; height: 46px; border-radius: 50%;
    background: var(--accent-orange);
    flex: none;
  }
  .brand__name {
    font-family: "Open Sans", sans-serif;
    font-weight: 600;
    font-size: 28px;
    line-height: 1.15;
    color: var(--ink);
  }
  .contact {
    position: absolute;
    left: 330px; top: 92px;
  }
  .contact__name {
    font-family: "Dancing Script", cursive;
    font-weight: 700;
    font-size: 46px;
    line-height: 1;
    color: var(--ink);
  }
  .contact__role { font-size: 15px; color: var(--ink-soft); margin-top: 6px; }
  .contact__lines { margin-top: 34px; font-size: 16px; line-height: 1.6; }
  .contact__lines b { font-weight: 600; }
  .contact__notes { margin-top: 30px; font-size: 15px; line-height: 1.7; color: var(--ink-soft); }
</style>
</head>
<body>
  <article class="card">
    <svg class="card__band" viewBox="0 0 840 480" aria-hidden="true">
      <defs>
        <linearGradient id="edgeAccent" x1="0" y1="0" x2="0" y2="1">
          <stop offset="0" stop-color="var(--accent-orange)" style="stop-color:#ee6a45"/>
          <stop offset="0.45" stop-color="#ee6a45"/>
          <stop offset="0.55" stop-color="#f2e21c"/>
          <stop offset="1" stop-color="#f2e21c"/>
        </linearGradient>
      </defs>
      <path d="M684 0 C624 120 744 300 644 480 L840 480 L840 0 Z" fill="url(#edgeAccent)"/>
      <path d="M697 0 C637 120 757 300 657 480 L840 480 L840 0 Z" fill="#ffffff"/>
      <path d="M701 0 C641 120 761 300 661 480 L840 480 L840 0 Z" fill="#262626"/>
    </svg>

    <div class="brand">
      <span class="brand__dot"></span>
      <span class="brand__name">Tidewell<br>Provisions</span>
    </div>

    <div class="contact">
      <h1 class="contact__name">Dean Holcroft</h1>
      <p class="contact__role">TK Wandsley Distributor</p>
      <p class="contact__lines">
        <b>T:</b> 317-640-8917<br>
        <b>E:</b> dean@tidewellprovisionsco.com
      </p>
      <p class="contact__notes">
        No minimum order<br>
        Gluten &amp; MSG free soup bases
      </p>
    </div>
  </article>
</body>
</html>
```